Web Application UI Design

Looking for a light weight UI re-design with complete html files and images for an existing project. As you can see from the uploaded files, the current design is clunky. We are looking to redesign the web application with state of the art light weight UI (Must include bootstrap and should be able to support angular)

Requirements
Must have
• Must have lightweight design preferably with material and bootstrap design
Nice to have
• The screen shots I uploaded show that the design is clunky. I am looking for some new designs

```html
<!DOCTYPE html>
<html lang="en">
<head>
<meta charset="UTF-8">
<title>DataPier – Ingestions Overview</title>
<link href="https://fonts.googleapis.com/css2?family=Nunito+Sans:wght@400;600;700&display=swap" rel="stylesheet">
<style>
  :root{
    --brand:#2633d9;
    --brand-dark:#1d29c4;
    --brand-deep:#1a24b0;
    --page:#f4f5f9;
    --card:#ffffff;
    --ink:#1f2233;
    --ink-soft:#3a3d4f;
    --muted:#8a8fa3;
    --line:#e8eaf1;
    --search:#f1f2f6;
    --green:#2ecc71;
    --red:#ef3b3b;
  }
  *{box-sizing:border-box;margin:0;padding:0}
  html,body{width:1200px;height:675px;overflow:hidden}
  body{font-family:"Nunito Sans",Arial,sans-serif;background:var(--page);color:var(--ink);position:relative}

  .sidebar{position:absolute;left:0;top:0;width:188px;height:675px;background:linear-gradient(180deg,var(--brand) 0%,var(--brand-dark) 100%);color:#fff}
  .brand{position:absolute;left:50px;top:14px;font-size:13px;font-weight:700}
  .nav{position:absolute;top:118px;left:0;right:0;list-style:none}
  .nav-item{height:36px;display:flex;align-items:center;padding-left:22px;font-size:13px;font-weight:600;position:relative}
  .nav-item svg{width:15px;height:15px;margin-right:13px;flex:none}
  .nav-item .chev{position:absolute;right:36px;width:9px;height:9px;margin:0}
  .subnav{list-style:none}
  .sub-item{height:33px;display:flex;align-items:center;padding-left:50px;font-size:12px;font-weight:600}
  .sub-item.active{background:#fff;color:var(--brand)}
  .sub-item.dim{background:var(--brand-deep)}
  .nav-item.gap{margin-top:10px}

  .topbar{position:absolute;left:188px;top:0;right:0;height:45px;background:#fff;border-bottom:1px solid var(--line)}
  .search{position:absolute;left:46px;top:6px;width:546px;height:32px;background:var(--search);border-radius:4px;display:flex;align-items:center;padding-left:14px;font-size:11px;color:var(--muted)}
  .search svg{width:12px;height:12px;margin-right:9px}
  .user{position:absolute;right:40px;top:6px;display:flex;align-items:center;font-size:13px;font-weight:600}
  .avatar{width:32px;height:32px;border-radius:50%;background:radial-gradient(circle at 50% 40%,#6b4a3a,#2a1e1a);margin-left:16px;border:2px solid #e9e9ee}

  .page-title{position:absolute;left:234px;top:66px;font-size:16px;font-weight:700}
  .page-size{position:absolute;left:234px;top:104px;display:flex;align-items:center;font-size:12px;font-weight:600;color:var(--ink-soft)}
  .select{margin:0 10px;width:46px;height:24px;border:1px solid var(--line);background:#fff;border-radius:3px;display:flex;align-items:center;justify-content:space-between;padding:0 7px 0 9px;color:var(--brand);font-weight:700}
  .select svg{width:7px;height:7px}
  .btn-create{position:absolute;left:1046px;top:101px;width:104px;height:30px;border:none;background:var(--brand);color:#fff;border-radius:4px;font:700 11px "Nunito Sans",Arial,sans-serif;box-shadow:0 3px 8px rgba(38,51,217,.3)}

  .table-card{position:absolute;left:234px;top:150px;width:916px;height:418px;background:var(--card);border-radius:6px;box-shadow:0 2px 8px rgba(30,35,90,.06)}
  table{width:100%;border-collapse:collapse;font-size:11.5px;table-layout:fixed}
  th{height:40px;text-align:left;font-weight:700;color:var(--ink);border-bottom:1px solid var(--line)}
  td{height:37.7px;color:var(--ink-soft);border-bottom:1px solid var(--line);white-space:nowrap}
  tbody tr:last-child td{border-bottom:none}
  .c-name{padding-left:11px;width:241px}
  .c-src{width:113px}.c-tgt{width:110px}.c-by{width:136px}.c-mod{width:175px}
  .actions{display:flex;gap:27px;align-items:center;padding-left:7px}
  .actions svg{width:12px;height:12px;display:block}

  .summary{position:absolute;left:234px;top:584px;font-size:11.5px;font-weight:600;color:var(--ink-soft)}
  .summary b{color:var(--brand)}
  .pager{position:absolute;left:975px;top:580px;display:flex;align-items:center}
  .pg-arrow{width:25px;height:25px;border-radius:50%;background:var(--brand);display:flex;align-items:center;justify-content:center}
  .pg-arrow svg{width:11px;height:11px}
  .pg-pages{display:flex;margin:0 6px;background:#fff;border-radius:4px;box-shadow:0 1px 4px rgba(30,35,90,.1)}
  .pg{width:34px;height:20px;display:flex;align-items:center;justify-content:center;font-size:10px;font-weight:700;color:var(--ink-soft)}
  .pg.current{background:var(--brand);color:#fff;border-radius:4px}
</style>
</head>
<body>
  <svg width="0" height="0" style="position:absolute" aria-hidden="true">
    <defs>
      <symbol id="i-run" viewBox="0 0 12 12"><path d="M3 1.8l7 4.2-7 4.2z" fill="none" stroke="#2ecc71" stroke-width="1.2" stroke-linejoin="round"/></symbol>
      <symbol id="i-stop" viewBox="0 0 12 12"><rect x="1.5" y="1.5" width="9" height="9" rx="1" fill="none" stroke="#ef3b3b" stroke-width="1.3"/></symbol>
      <symbol id="i-del" viewBox="0 0 12 12"><path d="M2 3h8M4.5 3V1.7h3V3M3 3l.6 7.5h4.8L9 3M5 5v4M7 5v4" fill="none" stroke="#ef3b3b" stroke-width="1.1"/></symbol>
    </defs>
  </svg>

  <aside class="sidebar">
    <div class="brand">DataPier</div>
    <ul class="nav">
      <li class="nav-item"><svg viewBox="0 0 16 16" fill="none" stroke="#fff" stroke-width="1.4"><circle cx="8" cy="8" r="2.5"/><path d="M8 1.5v2M8 12.5v2M1.5 8h2M12.5 8h2M3.4 3.4l1.4 1.4M11.2 11.2l1.4 1.4M3.4 12.6l1.4-1.4M11.2 4.8l1.4-1.4"/></svg>Services</li>
      <li class="nav-item"><svg viewBox="0 0 16 16" fill="none" stroke="#fff" stroke-width="1.4"><rect x="2" y="2" width="5" height="5" rx="1"/><rect x="9" y="2" width="5" height="5" rx="1"/><rect x="2" y="9" width="5" height="5" rx="1"/><rect x="9" y="9" width="5" height="5" rx="1"/></svg>Dashboard<svg class="chev" viewBox="0 0 10 10" fill="none" stroke="#fff" stroke-width="1.5"><path d="M2 3.5l3 3 3-3"/></svg></li>
      <li class="nav-item"><svg viewBox="0 0 16 16" fill="none" stroke="#fff" stroke-width="1.4"><path d="M6.5 9.5l3-3M7 4.5l1.5-1.5a2.5 2.5 0 013.5 3.5L10.5 8M9 11.5L7.5 13A2.5 2.5 0 014 9.5L5.5 8"/></svg>Connectors<svg class="chev" viewBox="0 0 10 10" fill="none" stroke="#fff" stroke-width="1.5"><path d="M2 3.5l3 3 3-3"/></svg></li>
      <li class="nav-item"><svg viewBox="0 0 16 16" fill="none" stroke="#fff" stroke-width="1.4"><circle cx="8" cy="5" r="2.8"/><path d="M2.5 14.5c.8-3 3-4.3 5.5-4.3s4.7 1.3 5.5 4.3"/></svg>Ingestion<svg class="chev" viewBox="0 0 10 10" fill="none" stroke="#fff" stroke-width="1.5"><path d="M2 6.5l3-3 3 3"/></svg></li>
      <li>
        <ul class="subnav">
          <li class="sub-item active">Overview</li>
          <li class="sub-item dim">Activity</li>
        </ul>
      </li>
      <li class="nav-item gap"><svg viewBox="0 0 16 16" fill="none" stroke="#fff" stroke-width="1.4"><rect x="2" y="3" width="12" height="10" rx="1"/><path d="M2 6h12"/></svg>WorkBench<svg class="chev" viewBox="0 0 10 10" fill="none" stroke="#fff" stroke-width="1.5"><path d="M2 3.5l3 3 3-3"/></svg></li>
      <li class="nav-item"><svg viewBox="0 0 16 16" fill="none" stroke="#fff" stroke-width="1.4"><circle cx="8" cy="5" r="2.8"/><path d="M2.5 14.5c.8-3 3-4.3 5.5-4.3s4.7 1.3 5.5 4.3"/></svg>Administration<svg class="chev" viewBox="0 0 10 10" fill="none" stroke="#fff" stroke-width="1.5"><path d="M2 3.5l3 3 3-3"/></svg></li>
    </ul>
  </aside>

  <header class="topbar">
    <div class="search"><svg viewBox="0 0 12 12" fill="none" stroke="#2633d9" stroke-width="1.4"><circle cx="5" cy="5" r="3.8"/><path d="M8 8l3 3"/></svg>Search Anything</div>
    <div class="user">Owen Hartley<div class="avatar" role="img" aria-label="User profile photo"></div></div>
  </header>

  <main>
    <h1 class="page-title">Ingestions Overview</h1>
    <div class="page-size">Show <span class="select">10<svg viewBox="0 0 8 8" fill="none" stroke="#8a8fa3" stroke-width="1.2"><path d="M1 2.5l3 3 3-3"/></svg></span> Entries per page</div>
    <button class="btn-create">Create Now</button>

    <section class="table-card">
      <table>
        <thead>
          <tr><th class="c-name">Name</th><th class="c-src">Source</th><th class="c-tgt">Target</th><th class="c-by">Created By</th><th class="c-mod">Last Modified</th><th>Actions</th></tr>
        </thead>
        <tbody>
          <tr><td class="c-name">SirinDemo</td><td>RDBMS</td><td>STRATA - SDFS</td><td>Neil Ashworth</td><td>23/12/2018 - 10:14</td><td><div class="actions"><svg><use href="#i-run"/></svg><svg><use href="#i-stop"/></svg><svg><use href="#i-del"/></svg></div></td></tr>
          <tr><td class="c-name">UdayDemo</td><td>RDBMS</td><td>STRATA - SDFS</td><td>Dale Morrow</td><td>02/01/2019 - 16:22</td><td><div class="actions"><svg><use href="#i-run"/></svg><svg><use href="#i-stop"/></svg><svg><use href="#i-del"/></svg></div></td></tr>
          <tr><td class="c-name">LastDayDemo</td><td>RDBMS</td><td>STRATA - SDFS</td><td>Colin Vance</td><td>14/03/2019 - 20:12</td><td><div class="actions"><svg><use href="#i-run"/></svg><svg><use href="#i-stop"/></svg><svg><use href="#i-del"/></svg></div></td></tr>
          <tr><td class="c-name">CalliDemo</td><td>RDBMS</td><td>STRATA - SDFS</td><td>Grant Ellery</td><td>15/03/2019 - 21:49</td><td><div class="actions"><svg><use href="#i-run"/></svg><svg><use href="#i-stop"/></svg><svg><use href="#i-del"/></svg></div></td></tr>
          <tr><td class="c-name">ForzaDevDemo</td><td>RDBMS</td><td>STRATA - SDFS</td><td>Marcus Whitfield</td><td>29/11/2018 - 22:30</td><td><div class="actions"><svg><use href="#i-run"/></svg><svg><use href="#i-stop"/></svg><svg><use href="#i-del"/></svg></div></td></tr>
          <tr><td class="c-name">Calli</td><td>RDBMS</td><td>STRATA - SHVS</td><td>Perry Lowden</td><td>29/01/2019 - 23:44</td><td><div class="actions"><svg><use href="#i-run"/></svg><svg><use href="#i-stop"/></svg><svg><use href="#i-del"/></svg></div></td></tr>
          <tr><td class="c-name">ForzaDev</td><td>RDBMS</td><td>STRATA - SHVS</td><td>Victor Ramsey</td><td>04/02/2019 - 15:25</td><td><div class="actions"><svg><use href="#i-run"/></svg><svg><use href="#i-stop"/></svg><svg><use href="#i-del"/></svg></div></td></tr>
          <tr><td class="c-name">Calli55</td><td>RDBMS</td><td>STRATA - SHVS</td><td>Ian Sutter</td><td>10/12/2018 - 19:44</td><td><div class="actions"><svg><use href="#i-run"/></svg><svg><use href="#i-stop"/></svg><svg><use href="#i-del"/></svg></div></td></tr>
          <tr><td class="c-name">Calli55</td><td>RDBMS</td><td>STRATA - SDFS</td><td>Felix Hardin</td><td>05/12/2018 - 03:15</td><td><div class="actions"><svg><use href="#i-run"/></svg><svg><use href="#i-stop"/></svg><svg><use href="#i-del"/></svg></div></td></tr>
          <tr><td class="c-name">Calli55</td><td>RDBMS</td><td>STRATA - SDFS</td><td>Rory Keeling</td><td>24/07/2018 - 14:45</td><td><div class="actions"><svg><use href="#i-run"/></svg><svg><use href="#i-stop"/></svg><svg><use href="#i-del"/></svg></div></td></tr>
        </tbody>
      </table>
    </section>

    <p class="summary">Showing <b>10</b> of <b>33</b> Entries</p>
    <nav class="pager">
      <span class="pg-arrow"><svg viewBox="0 0 12 12" fill="none" stroke="#fff" stroke-width="1.6"><path d="M10 6H2M5 3L2 6l3 3"/></svg></span>
      <span class="pg-pages"><span class="pg current">01</span><span class="pg">02</span><span class="pg">03</span></span>
      <span class="pg-arrow"><svg viewBox="0 0 12 12" fill="none" stroke="#fff" stroke-width="1.6"><path d="M2 6h8M7 3l3 3-3 3"/></svg></span>
    </nav>
  </main>
</body>
</html>
```